Business card for apparel company. Specializing in fishing and boating performance wear. Main company name is Palmetto Heron Company, LLC brand name for apparel is TIDEMARK. See website www.TidemarkBayline.com I will attach some logos to consider.

```html
<!DOCTYPE html>
<html lang="en">
<head>
<meta charset="utf-8">
<title>Tidemark Business Card</title>
<link href="https://fonts.googleapis.com/css2?family=Montserrat:wght@400;500;800&display=swap" rel="stylesheet">
<style>
  :root {
    --page-bg: #e4e4e4;
    --card-white: #ffffff;
    --brand-light: #1ea3de;
    --brand-deep: #3869b8;
    --brand-mid: #2a8fd6;
    --ink: #1d1d1d;
  }
  * { margin: 0; padding: 0; box-sizing: border-box; }
  html, body {
    width: 1200px; height: 856px; overflow: hidden;
    background: var(--page-bg);
    font-family: "Montserrat", sans-serif;
  }
  .canvas {
    position: relative; width: 1200px; height: 856px;
    display: flex; align-items: center; justify-content: center; gap: 60px;
  }
  .card {
    position: relative; width: 520px; height: 297px; overflow: hidden;
    box-shadow: 0 10px 28px rgba(0,0,0,0.22);
  }
  .card--front { background: var(--card-white); }
  .card--back {
    background: linear-gradient(120deg, var(--brand-light) 0%, var(--brand-deep) 100%);
    display: flex; align-items: center; justify-content: center;
  }
  .brand-name {
    font-weight: 800; letter-spacing: 2px; line-height: 1;
  }
  .card--front .brand-name {
    position: absolute; left: 34px; top: 118px;
    font-size: 30px; color: var(--brand-mid);
  }
  .card--back .brand-name { font-size: 56px; color: #ffffff; }
  .divider {
    position: absolute; left: 228px; top: 70px;
    width: 1.5px; height: 106px; background: var(--brand-mid);
  }
  .contact {
    position: absolute; left: 246px; top: 64px;
    font-size: 12.5px; line-height: 20px; color: var(--ink); font-weight: 500;
    list-style: none;
  }
  .contact li { display: flex; align-items: center; gap: 7px; white-space: nowrap; }
  .contact .icon { width: 12px; height: 12px; flex: none; }
  .bands { position: absolute; left: 0; bottom: 0; }
  .website {
    position: absolute; right: 20px; bottom: 16px;
    font-size: 12.5px; color: #ffffff; font-weight: 400; letter-spacing: 0.4px;
  }
</style>
</head>
<body>
<main class="canvas">
  <section class="card card--front">
    <div class="brand-name">TIDEMARK</div>
    <div class="divider"></div>
    <ul class="contact">
      <li>Palmetto Heron Company, LLC</li>
      <li>P.O. Box 418</li>
      <li>Crestview Shoals, Florida 34011</li>
      <li>
        <svg class="icon" viewBox="0 0 12 12"><path d="M2.5 1h2l1 2.5-1.3 1a6 6 0 0 0 3.3 3.3l1-1.3L11 7.5v2c0 .8-.7 1.5-1.5 1.5A9 9 0 0 1 1 2.5C1 1.7 1.7 1 2.5 1z" fill="var(--brand-mid)"/></svg>
        # 555-014-2290
      </li>
      <li>
        <svg class="icon" viewBox="0 0 12 12"><rect x="0.5" y="2" width="11" height="8" rx="1" fill="var(--brand-mid)"/><path d="M1 2.5l5 4 5-4" stroke="#fff" stroke-width="1" fill="none"/></svg>
        info@PalmettoHeronCo.com
      </li>
    </ul>
    <svg class="bands" width="520" height="297" viewBox="0 0 520 297">
      <defs>
        <linearGradient id="bandGrad" x1="0" y1="0" x2="1" y2="0">
          <stop offset="0" stop-color="var(--brand-light)"/>
          <stop offset="1" stop-color="var(--brand-deep)"/>
        </linearGradient>
      </defs>
      <polygon points="0,286 520,286 520,297 0,297" fill="url(#bandGrad)"/>
      <polygon points="0,274 292,274 290,280 0,280" fill="url(#bandGrad)"/>
      <polygon points="300,246 520,246 520,282 292,282" fill="url(#bandGrad)"/>
    </svg>
    <div class="website">www.TidemarkBayline.com</div>
  </section>

  <section class="card card--back">
    <div class="brand-name">TIDEMARK</div>
  </section>
</main>
</body>
</html>
```